Security business needs NDA formatted.

We need our NDA formatted properly and to look modern with our logo. Anybody can paste words into a document, but we need something clean, modern, DocuSign-friendly, and stylish.

```html
<!DOCTYPE html>
<html lang="en">
<head>
<meta charset="utf-8">
<title>Non-Disclosure Agreement – Terravanta</title>
<link rel="stylesheet" href="https://fonts.googleapis.com/css2?family=Montserrat:wght@400;500;600;700&display=swap">
<style>
  :root {
    --ink: #1c1c1c;
    --paper: #ffffff;
    --accent: #ee1c37;
    --footer: #2a2a2a;
    --footer-text: #ffffff;
  }
  * { margin: 0; padding: 0; box-sizing: border-box; }
  html, body {
    width: 927px;
    height: 1200px;
    overflow: hidden;
    background: var(--paper);
  }
  .page {
    position: relative;
    width: 927px;
    height: 1200px;
    background: var(--paper);
    color: var(--ink);
    font-family: "Montserrat", sans-serif;
    font-size: 17.5px;
    letter-spacing: 0.2px;
  }
  .page > * { position: absolute; }

  /* Brand header */
  .brand-mark {
    left: 286px; top: 51px;
    width: 88px; height: 88px;
    border-radius: 50%;
    background: var(--ink);
  }
  .brand-name {
    left: 392px; top: 60px;
    font-size: 46px; font-weight: 700;
    letter-spacing: 0.5px;
    line-height: 1;
  }
  .brand-tagline {
    left: 404px; top: 110px;
    font-size: 14px; font-weight: 600;
    letter-spacing: 1.6px;
  }
  .header-rule {
    left: 100px; top: 183px;
    width: 727px; height: 2px;
    background: var(--ink);
  }
  .header-rule-accent {
    left: 282px; top: 182px;
    width: 376px; height: 4.5px;
    background: var(--accent);
  }

  /* Title and parties */
  .doc-title {
    left: 0; width: 927px; top: 243px;
    text-align: center;
    font-size: 21px; font-weight: 700;
    letter-spacing: 4.4px;
  }
  .preamble { left: 108px; top: 309px; line-height: 26px; }
  .preamble .indent { padding-left: 52px; }
  .blank {
    display: inline-block;
    width: 103px;
    border-bottom: 1.5px solid var(--ink);
    margin: 0 4px;
    height: 14px;
  }
  .between { left: 108px; top: 391px; }
  .party {
    left: 0; width: 927px;
    text-align: center;
    line-height: 27px;
  }
  .party--company { top: 465px; font-weight: 500; padding-left: 22px; }
  .party--evaluator { top: 656px; padding-left: 6px; }
  .party-joiner { left: 0; width: 927px; text-align: center; top: 602px; padding-left: -12px; }
  .party-role { text-align: right; }
  .party-role--first { right: 85px; top: 549px; }
  .party-role--second { right: 80px; top: 758px; }
  .role-underline { height: 2px; background: var(--accent); }
  .role-underline--first { left: 727px; top: 577px; width: 115px; }
  .role-underline--second { left: 755px; top: 786px; width: 88px; }

  /* Background section */
  .section-heading {
    left: 108px; top: 829px;
    font-weight: 700; font-size: 17px;
    letter-spacing: 0.6px;
  }
  .section-underline {
    left: 108px; top: 858px;
    width: 49px; height: 3px;
    background: var(--accent);
  }
  .recital { left: 108px; line-height: 27.4px; }
  .recital--a { top: 878px; }
  .recital--b { top: 960px; }

  /* Footer */
  .footer-band {
    left: 0; top: 1111px;
    width: 927px; height: 26px;
    background: var(--accent);
  }
  .footer-stripes { left: 0; top: 1111px; }
  .footer-bar {
    left: 0; top: 1137px;
    width: 927px; height: 63px;
    background: var(--footer);
  }
  .footer-text {
    top: 1161px;
    color: var(--footer-text);
    font-size: 13.5px;
  }
  .footer-copyright { left: 54px; }
  .footer-page { right: 55px; font-size: 14.5px; }
</style>
</head>
<body>
  <main class="page">
    <div class="brand-mark"></div>
    <div class="brand-name">Terravanta</div>
    <div class="brand-tagline">Geospatial Intelligence</div>
    <div class="header-rule"></div>
    <div class="header-rule-accent"></div>

    <h1 class="doc-title">NON-DISCLOSURE AGREEMENT</h1>

    <p class="preamble"><span class="indent">THIS NON-DISCLOSURE AGREEMENT ("the Agreement") dated</span><br>this<span class="blank"></span>day of <span class="blank" style="margin-left:10px"></span>,<span class="blank"></span>.</p>

    <p class="between">BETWEEN:</p>

    <p class="party party--company">ACME of 48 Harbor Lane, CA, 90210, USA (the "Company")</p>
    <p class="party-role party-role--first">OF THE FIRST PART</p>
    <div class="role-underline role-underline--first"></div>

    <p class="party-joiner">- AND -</p>

    <p class="party party--evaluator">COMPANY NAME of COMPANY ADDRESS<br><span style="padding-right:54px">(the "Evaluator")</span></p>
    <p class="party-role party-role--second">OF THE SECOND PART</p>
    <div class="role-underline role-underline--second"></div>

    <h2 class="section-heading">BACKGROUND:</h2>
    <div class="section-underline"></div>

    <p class="recital recital--a">A.&nbsp; ACME has proprietary information and know-how relating to certain<br>investigation tools and tactics (the "Company").</p>
    <p class="recital recital--b">B.&nbsp; In connection with the Evaluator evaluating the Invention for possible patent,<br>development, and marketing (the "Permitted Purpose"), the Evaluatorhas<br>requested certain confidential information (the "Confidential Information")<br>regarding the Company.</p>

    <div class="footer-band"></div>
    <svg class="footer-stripes" width="927" height="26" viewBox="0 0 927 26" aria-hidden="true">
      <polygon points="798,0 809,0 790,26 779,26" fill="#ffffff"/>
      <polygon points="820,0 832,0 813,26 801,26" fill="#ffffff"/>
    </svg>
    <div class="footer-bar"></div>
    <p class="footer-text footer-copyright">©2002-2022 FormHarbor.com®</p>
    <p class="footer-text footer-page">Page 1 of 9</p>
  </main>
</body>
</html>
```